Medigap Insurance Interactive website

We are looking at redesigning our website for a more up to date and responsive look and feel. We will code this site using Bootstrap 3 so please research and know how to design for this. Attached is our logo and a wireframe for the new site.
I look forward to seeing what you guys can do.

Target Market(s)

People elegible for Medigap Insurance in the US

Industry/Entity Type

Insurance

Number of Pages Required

5+ page

Font styles to use
Sans Serif

Requirements
Must have
• Match the logo
• Be Bootstrap 3 compatible design
• Font Awesome Icons

```html
<!DOCTYPE html>
<html lang="en">
<head>
<meta charset="utf-8">
<title>Harborline – Interactive real time rate quote</title>
<link href="https://fonts.googleapis.com/css2?family=Arimo:wght@400;700&display=swap" rel="stylesheet">
<style>
:root{
  --red:#b32019;
  --navy:#0c2d5e;
  --navy-deep:#002a5c;
  --ink:#222;
  --muted:#444;
  --line:#d6d6d6;
  --footer:#e0e0e0;
  --white:#fff;
}
*{box-sizing:border-box;margin:0;padding:0}
html,body{width:1200px;height:802px;overflow:hidden;background:var(--white);font-family:"Arimo",Arial,sans-serif;color:var(--ink)}
.site-header{position:relative;height:65px;border-bottom:1px solid var(--line)}
.brand{position:absolute;left:38px;top:22px;font-size:20px;font-weight:700;color:var(--navy);letter-spacing:.5px;line-height:1}
.main-nav{position:absolute;left:216px;top:0;height:65px;display:flex}
.main-nav a{display:flex;align-items:center;height:65px;padding:0 2px;margin-right:15px;font-size:12px;font-weight:700;color:var(--ink);text-decoration:none;position:relative;white-space:nowrap}
.main-nav a:last-child{margin-right:0}
.main-nav a.active::after{content:"";position:absolute;left:0;right:0;bottom:0;height:3px;background:var(--red)}
.contact{position:absolute;left:898px;top:0;width:204px;height:65px;border-left:1px solid var(--line);border-right:1px solid var(--line);text-align:center;padding-top:14px}
.contact .cta{font-size:13.5px;font-weight:700;color:var(--red);display:block}
.contact .phone{font-size:15.5px;color:var(--muted);display:block;margin-top:5px;letter-spacing:.4px}
.social{position:absolute;left:1118px;top:14px;display:grid;grid-template-columns:19px 19px;gap:5px 9px}
.social span{width:19px;height:19px;border-radius:4px;background:var(--ink)}
.hero{height:189px;background:linear-gradient(135deg,#123a6e 0%,#0d2f5f 50%,#143d72 100%);display:flex;flex-direction:column;align-items:center;justify-content:center}
.hero h1{color:var(--white);font-size:32px;font-weight:700;letter-spacing:.6px;margin-top:-4px}
.hero .rule{width:514px;height:3px;background:var(--red);margin-top:18px}
.quote-card{position:absolute;left:281px;top:342px;width:609px;height:248px;background:var(--red);border-radius:8px;padding:13px}
.quote-inner{height:100%;border:1px solid rgba(255,255,255,.35);border-radius:10px;text-align:center;padding-top:38px}
.quote-inner h2{color:var(--white);font-size:28px;font-weight:400;letter-spacing:-.6px}
.quote-form{display:flex;justify-content:center;gap:18px;margin-top:40px}
.quote-form input{width:202px;height:47px;border:1px solid #333;padding:0 14px;font:15px "Arimo",Arial,sans-serif;color:var(--ink);outline:none}
.quote-form input::placeholder{color:#aaa}
.quote-form button{width:141px;height:47px;border:0;background:var(--navy-deep);color:var(--white);font:18px "Arimo",Arial,sans-serif}
.site-footer{position:absolute;left:0;top:721px;width:1200px;height:44px;background:var(--footer);display:flex;justify-content:center;align-items:center;font-size:13.5px;color:var(--muted)}
.site-footer a{color:var(--muted);text-decoration:none}
.site-footer .sep{margin:0 22px}
</style>
</head>
<body>
<header class="site-header">
  <div class="brand">HARBORLINE</div>
  <nav class="main-nav">
    <a href="#" class="active">MEDICARE SUPPLEMENT</a>
    <a href="#">PART D</a>
    <a href="#">HOW TO DECIDE</a>
    <a href="#">LEARN ONLINE</a>
    <a href="#">WHY HARBORLINE</a>
    <a href="#">BUY NOW</a>
  </nav>
  <div class="contact">
    <span class="cta">COMPARE RATES &amp; SAVE</span>
    <span class="phone">(888) 555-0142</span>
  </div>
  <div class="social" aria-label="Social links">
    <span></span><span></span><span></span><span></span>
  </div>
</header>
<section class="hero" role="img" aria-label="Dark blue tinted photo of people working at a desk with laptops and papers">
  <h1>Interactive real time rate quote</h1>
  <div class="rule"></div>
</section>
<section class="quote-card">
  <div class="quote-inner">
    <h2>Start with searching by your zip code</h2>
    <form class="quote-form">
      <input type="text" placeholder="Zipcode">
      <button type="button">Find Quotes</button>
    </form>
  </div>
</section>
<footer class="site-footer">
  <a href="#">Harborline</a><span class="sep">|</span>
  <a href="#">Sitemap</a><span class="sep">|</span>
  <a href="#">Buy Now</a><span class="sep">|</span>
  <a href="#">Blog</a><span class="sep">|</span>
  <a href="#">Login</a>
</footer>
</body>
</html>
```